Business Card Design

Lawyer
Business name "HallorenLaw"
Areas of expertise:
property
commercial
trusts
immigration
franchising
I want the following quote on the back of the card somewhere.
"Education is when you read the fine print,
experience is what you get if you don't." Clem Varnody
Probably the "areas of expertise" should be on the back also to avoid cluttering the front.
As for colours, I like the shades of blue used on qelvobank.com.
The basic part of the card with the contact info needs to be white and uncluttered.
Target Market(s)
small to medium sized self employed business people
Industry/Entity Type
Business
Contact Information for Business Card
Dwight Halloren
Phone + 64 9 415 3067
Fax: + 64 9 415 3066
PO Box 742
Kelverton
Wainuiroa 3915
NZ
email: dwight@ferncastlaw.example.co.nz

```html
<!DOCTYPE html>
<html lang="en">
<head>
<meta charset="utf-8">
<title>HallorenLaw Business Card</title>
<link rel="stylesheet" href="https://fonts.googleapis.com/css2?family=Questrial&display=swap">
<style>
  :root {
    --stage: #6a6a6b;
    --paper: #f8f8f8;
    --ink: #151515;
    --brand-blue: #0a86c8;
    --accent-blue: #1a8fd0;
    --band-blue: #005a8c;
    --panel-dark: #1f1f21;
    --panel-black: #050505;
    --rule-grey: #8a8a8a;
    --white: #ffffff;
  }
  * { margin: 0; padding: 0; box-sizing: border-box; }
  html, body {
    width: 919px; height: 1200px; overflow: hidden;
    background: var(--stage);
    font-family: "Questrial", "Century Gothic", sans-serif;
  }
  .canvas { position: relative; width: 919px; height: 1200px; }

  .card {
    position: absolute; left: 88px; width: 780px; height: 487px;
    background: var(--paper); overflow: hidden;
  }
  .card--front { top: 97px; }
  .card--back { top: 624px; }

  .brand {
    position: absolute; left: 0; right: 0;
    display: flex; align-items: center; justify-content: center; gap: 18px;
  }
  .card--front .brand { top: 70px; }
  .card--back .brand { top: 72px; }
  .brand__square { width: 38px; height: 38px; background: var(--brand-blue); }
  .brand__name {
    color: var(--brand-blue); font-size: 66px; line-height: 1;
    letter-spacing: 1px;
  }

  /* front */
  .front__band { position: absolute; left: 0; top: 219px; width: 100%; height: 24px; background: var(--band-blue); }
  .front__panel { position: absolute; left: 0; top: 243px; width: 100%; height: 244px; background: var(--panel-dark); }
  .person__name { position: absolute; left: 57px; top: 331px; color: var(--accent-blue); font-size: 33px; }
  .person__role { position: absolute; left: 128px; top: 371px; color: var(--white); font-size: 26px; }
  .front__divider { position: absolute; left: 354px; top: 281px; width: 1px; height: 178px; background: var(--rule-grey); }
  .contact { position: absolute; left: 427px; color: var(--white); font-size: 19px; line-height: 1; white-space: nowrap; }
  .contact__label { color: var(--accent-blue); display: inline-block; width: 83px; font-size: 18px; }
  .contact__value { font-size: 17px; }
  .contact--addr1 { top: 297px; }
  .contact--addr2 { top: 320px; }
  .contact--phone { top: 355px; }
  .contact--fax { top: 383px; }
  .contact--email { top: 412px; }
  .contact--email .contact__label { width: 91px; }
  .contact--email .contact__value { font-size: 15px; }

  /* back */
  .expertise__title {
    position: absolute; left: 24px; top: 261px;
    color: var(--accent-blue); font-size: 21px; font-weight: 400; letter-spacing: 2px;
  }
  .expertise__list { position: absolute; list-style: none; color: var(--ink); font-size: 22px; letter-spacing: 1.8px; line-height: 28.5px; }
  .expertise__list--left { left: 23px; top: 292px; }
  .expertise__list--right { left: 517px; top: 297px; line-height: 26px; }
  .back__rule { position: absolute; left: 0; top: 399px; width: 100%; height: 9px; background: var(--band-blue); }
  .back__panel { position: absolute; left: 0; top: 408px; width: 100%; height: 79px; background: var(--panel-black); }
  .quote {
    position: absolute; left: 10px; top: 413px; width: 768px;
    color: var(--white); font-size: 21px; letter-spacing: 3.1px; line-height: 31px;
  }
  .quote__author { color: var(--accent-blue); }
</style>
</head>
<body>
<main class="canvas">
  <section class="card card--front">
    <div class="brand">
      <span class="brand__square"></span>
      <span class="brand__name">HallorenLaw</span>
    </div>
    <div class="front__band"></div>
    <div class="front__panel"></div>
    <p class="person__name">Dwight Halloren</p>
    <p class="person__role">Designation</p>
    <div class="front__divider"></div>
    <p class="contact contact--addr1">PO Box 742 Kelverton</p>
    <p class="contact contact--addr2">Wainuiroa 3915 NZ</p>
    <p class="contact contact--phone"><span class="contact__label">Phone :</span><span class="contact__value">+ 64 9 415 3067</span></p>
    <p class="contact contact--fax"><span class="contact__label">Fax&nbsp;&nbsp;&nbsp;&nbsp;&nbsp;:</span><span class="contact__value">+ 64 9 415 3066</span></p>
    <p class="contact contact--email"><span class="contact__label">email&nbsp;&nbsp;:</span><span class="contact__value">dwight@ferncastlaw.example.co.nz</span></p>
  </section>

  <section class="card card--back">
    <div class="brand">
      <span class="brand__square"></span>
      <span class="brand__name">HallorenLaw</span>
    </div>
    <h2 class="expertise__title">AREAS OF EXPERTISE</h2>
    <ul class="expertise__list expertise__list--left">
      <li>Property</li>
      <li>Commercial trusts</li>
      <li>Trusts</li>
    </ul>
    <ul class="expertise__list expertise__list--right">
      <li>Immigration</li>
      <li>Franchising</li>
    </ul>
    <div class="back__rule"></div>
    <div class="back__panel"></div>
    <p class="quote">Education is when you read the fine print, experience<br>is what you get if you don't.<span class="quote__author">" Clem Varnody "</span></p>
  </section>
</main>
</body>
</html>
```